Business card for a shipping supplies business

Needing a business card design. Please see the logo. The logo with the white font should be used if there is a dark background.

We are looking for the following info on the card. Please see the sample info. We will need the info to be changed with a few different employee names and info but all will use the same template.

Business Name: The Crate Heron
Employee Name : Marcus Delaney
Position: Account Manager
Address: 4827 W. Ridge 418 S.
Fort Worth, TX 73948
email: Marcus@thecrateheron.example
telephone: 855-619-2740 x 207
website: www.getparcelkits.example

Target Market(s)

Businesses who ship products for online sales

Industry/Entity Type

Cardboard

Contact Information for Business Card

Name, title, address, website, logo, telephone number

Font styles to use
Sans Serif

Colors
EE7325
F08F49
F5BC92
FAE3D3
FDF4ED

Requirements
Must have
• Logo on back of card. Clean look, just logo, website address

```html
<!DOCTYPE html>
<html lang="en">
<head>
<meta charset="utf-8">
<title>The Crate Heron – Business Card</title>
<link rel="stylesheet" href="https://fonts.googleapis.com/css2?family=Montserrat:wght@400;500;700&display=swap">
<style>
  :root {
    --stage: #3a3a3a;
    --card: #1b1b1b;
    --card-deep: #151515;
    --orange: #ee7325;
    --orange-soft: #f08f49;
    --peach: #f5bc92;
    --white: #f4f4f4;
    --pattern-a: #1e1e1e;
    --pattern-b: #262626;
  }
  * { margin: 0; padding: 0; box-sizing: border-box; }
  html, body {
    width: 1200px; height: 801px; overflow: hidden;
    background: var(--stage);
    font-family: "Montserrat", sans-serif;
  }
  .stage { position: relative; width: 1200px; height: 801px; }

  .card {
    position: absolute;
    width: 540px; height: 309px;
    background: var(--card);
    border-bottom: 3px solid var(--orange);
    box-shadow: 0 18px 40px rgba(0,0,0,.45);
    overflow: hidden;
  }
  .card--front { left: 50px; top: 120px; }
  .card--back { left: 610px; top: 372px; }

  /* Front */
  .brand {
    position: absolute; left: 40px; top: 0; bottom: 0; width: 220px;
    display: flex; align-items: center; gap: 12px;
  }
  .brand__dot {
    width: 26px; height: 26px; border-radius: 50%;
    background: var(--orange); flex: none;
  }
  .brand__name {
    color: var(--white); font-weight: 700; font-size: 24px;
    line-height: 1.1; letter-spacing: .5px;
  }
  .divider {
    position: absolute; left: 272px; top: 50px; width: 1px; height: 210px;
    background: var(--orange);
  }
  .contact {
    position: absolute; left: 296px; top: 50px; right: 16px;
    color: var(--white); font-size: 12.5px; line-height: 1.45;
  }
  .contact__name {
    color: var(--orange); font-weight: 700; font-size: 19px;
    text-transform: uppercase; letter-spacing: .3px; line-height: 1.2;
  }
  .contact__title { font-size: 13.5px; margin-bottom: 14px; }
  .contact__address { margin-bottom: 14px; }
  .contact__list { list-style: none; }
  .contact__item { display: flex; align-items: center; gap: 8px; white-space: nowrap; font-size: 12px; }
  .contact__icon { width: 11px; height: 11px; flex: none; }

  /* Back */
  .pattern {
    position: absolute; inset: 0;
    background:
      repeating-linear-gradient(45deg, var(--pattern-a) 0 34px, var(--pattern-b) 34px 68px);
    opacity: .9;
  }
  .back-mark {
    position: absolute; right: 42px; top: 150px;
    display: flex; align-items: center; gap: 6px;
    background: var(--card-deep); padding: 6px 8px;
  }
  .back-mark__dot { width: 10px; height: 10px; border-radius: 50%; background: var(--orange); }
  .back-mark__name { color: var(--orange); font-weight: 700; font-size: 11px; }
</style>
</head>
<body>
<main class="stage">
  <section class="card card--front" aria-label="Business card front">
    <div class="brand">
      <span class="brand__dot"></span>
      <span class="brand__name">The Crate Heron</span>
    </div>
    <div class="divider"></div>
    <div class="contact">
      <p class="contact__name">Marcus Delaney</p>
      <p class="contact__title">Account Manager</p>
      <p class="contact__address">4827 W. Ridge 418 S.<br>Fort Worth, TX 73948</p>
      <ul class="contact__list">
        <li class="contact__item">
          <svg class="contact__icon" viewBox="0 0 12 12"><circle cx="6" cy="6" r="6" fill="#f5bc92"/><path d="M4 3.2l1 1.6-.6.6c.4.8 1 1.4 1.8 1.8l.6-.6 1.6 1-.5 1.2C5.7 8.6 3.4 6.3 3.2 4z" fill="#1b1b1b"/></svg>
          855-619-2740 x 207
        </li>
        <li class="contact__item">
          <svg class="contact__icon" viewBox="0 0 12 12"><rect x="1" y="2.5" width="10" height="7" rx="1" fill="#f5bc92"/><path d="M1.5 3l4.5 3.5L10.5 3" fill="none" stroke="#1b1b1b" stroke-width="1"/></svg>
          Marcus@thecrateheron.example
        </li>
        <li class="contact__item">
          <svg class="contact__icon" viewBox="0 0 12 12"><circle cx="6" cy="6" r="5" fill="none" stroke="#f5bc92" stroke-width="1.4"/><path d="M1 6h10M6 1c2 2.5 2 7.5 0 10M6 1c-2 2.5-2 7.5 0 10" fill="none" stroke="#f5bc92" stroke-width="1"/></svg>
          www.getparcelkits.example
        </li>
      </ul>
    </div>
  </section>

  <section class="card card--back" aria-label="Business card back">
    <div class="pattern" role="img" aria-label="Tonal repeating pattern of the brand symbol, spot-gloss black on black"></div>
    <div class="back-mark">
      <span class="back-mark__dot"></span>
      <span class="back-mark__name">The Crate Heron</span>
    </div>
  </section>
</main>
</body>
</html>
```